Business Card Design - Carrington Hill Lodge

We are looking at a new design for our business cards that has a modern and professional look. We run a residential aged care facility focussing on the care of residents. The cards will be used for potential clients, consultants and business opportunities in this sector. Blue and white is our main colours and would to see these colours incorporated in the design.
Industry/Entity Type
Business
Contact Information for Business Card
Carrington Hill Lodge, Darren Pelham, dpelham@carringtonhilllodge.com.au, Finance Manager, 0491 736 208, BCom, 48 Yarrabee Way, Bellmere Park, Qld 4510.

```html
<!DOCTYPE html>
<html lang="en">
<head>
<meta charset="utf-8">
<title>Carrington Hill Lodge – Business Cards</title>
<link rel="stylesheet" href="https://fonts.googleapis.com/css2?family=Open+Sans:wght@400;600&display=swap">
<style>
  :root {
    --backdrop: #e8e8e6;
    --card: #ffffff;
    --brand-blue: #3f6e8c;
    --ink: #2b2b2b;
    --muted: #555b60;
    --icon-ring: #2b2b2b;
  }
  * { margin: 0; padding: 0; box-sizing: border-box; }
  html, body {
    width: 1200px;
    height: 873px;
    overflow: hidden;
    background: var(--backdrop);
    font-family: "Open Sans", Arial, sans-serif;
  }
  .sheet {
    position: relative;
    width: 1200px;
    height: 873px;
    display: flex;
    align-items: center;
    justify-content: center;
    gap: 60px;
  }
  .card {
    width: 520px;
    height: 316px;
    background: var(--card);
    box-shadow: 0 2px 10px rgba(0,0,0,0.12);
    position: relative;
    overflow: hidden;
  }
  .card svg { display: block; }
  .brand-panel { fill: var(--brand-blue); }
  .brand-disc { fill: #ffffff; }
  .brand-name {
    fill: #ffffff;
    font-size: 14px;
    font-weight: 600;
    letter-spacing: 0.3px;
  }
  .icon-ring { fill: #ffffff; stroke: var(--icon-ring); stroke-width: 1.4; }
  .icon-glyph { fill: var(--ink); }
  .icon-line { fill: none; stroke: var(--ink); stroke-width: 1.5; stroke-linecap: round; }
  .holder-name { fill: var(--brand-blue); font-size: 14px; font-weight: 600; }
  .holder-title { fill: var(--muted); font-size: 12px; }
  .contact-line { fill: var(--ink); font-size: 12px; }
</style>
</head>
<body>
<main class="sheet">

  <section class="card card--back" aria-label="Business card back">
    <svg width="520" height="316" viewBox="0 0 520 316">
      <path class="brand-panel" d="M0 0 H130 A200 200 0 0 1 130 316 H0 Z"/>
      <circle class="brand-disc" cx="92" cy="118" r="40"/>
      <text class="brand-name" x="92" y="190" text-anchor="middle">Carrington Hill Lodge</text>

      <g class="icon icon--email" transform="translate(207 158)">
        <circle class="icon-ring" r="11"/>
        <rect class="icon-line" x="-6" y="-4.5" width="12" height="9" rx="1"/>
        <path class="icon-line" d="M-6 -4 L0 1 L6 -4"/>
      </g>
      <text class="contact-line" x="235" y="162">dpelham@carringtonhilllodge.com.au</text>
    </svg>
  </section>

  <section class="card card--front" aria-label="Business card front">
    <svg width="520" height="316" viewBox="0 0 520 316">
      <path class="brand-panel" d="M0 0 H130 A200 200 0 0 1 130 316 H0 Z"/>
      <circle class="brand-disc" cx="92" cy="118" r="40"/>
      <text class="brand-name" x="92" y="190" text-anchor="middle">Carrington Hill Lodge</text>

      <g class="icon icon--person" transform="translate(197 95)">
        <circle class="icon-ring" r="11"/>
        <circle class="icon-glyph" cx="0" cy="-2.5" r="3"/>
        <path class="icon-glyph" d="M-5.5 6 C-5.5 1.5 5.5 1.5 5.5 6 Z"/>
      </g>
      <text class="holder-name" x="235" y="96">Carrington Hill Lodge, Darren Pelham</text>
      <text class="holder-title" x="235" y="114">Finance Manager</text>

      <g class="icon icon--phone" transform="translate(207 150)">
        <circle class="icon-ring" r="11"/>
        <path class="icon-glyph" d="M-5 -5.5 L-2.5 -6 L-1 -2.5 L-2.6 -1.2 C-1.8 0.6 -0.6 1.8 1.2 2.6 L2.5 1 L6 2.5 L5.5 5 C1 6 -6 -1 -5 -5.5 Z"/>
      </g>
      <text class="contact-line" x="235" y="154">0491 736 208</text>

      <g class="icon icon--pin" transform="translate(202 205)">
        <circle class="icon-ring" r="11"/>
        <path class="icon-glyph" d="M0 6.5 C-3 2.5 -4.5 0 -4.5 -2 A4.5 4.5 0 0 1 4.5 -2 C4.5 0 3 2.5 0 6.5 Z"/>
        <circle cx="0" cy="-2" r="1.6" fill="#ffffff"/>
      </g>
      <text class="contact-line" x="235" y="209">48 Yarrabee Way, Bellmere Park, Qld 4510</text>
    </svg>
  </section>

</main>
</body>
</html>
```